Neues Corporate Design für Steuerberaterin
Zielgruppe
Ich bin seit Kurzem als Steuerberaterin selbständig tätig. Meine Zielgruppe sind v.a. junge engagierte Leute zwischen 25 und 45 Jahren - Privatpersonen als auch Unternehmer - die ein bisschen anders denken und sich beim herkömmlichen Steuerberater nicht gut aufgehoben fühlen. Mir ist auch der persönliche/menschliche Aspekt mit meinen Kunden sehr wichtig (im Gegensatz zu vielen anderen), denn fachlich top sind eh die meisten und mein Eindruck ist, das alleine reicht nicht mehr aus.
Aufgabenstellung
Ich habe mich in den vergangenen Jahren bereits ein bisschen auf die Selbständigkeit vorbereitet und u.a. auch eine Visitenkarte entworfen (siehe Anhang). Allerdings ist das schon etwas länger her und ich finde diese 'alte' Visitenkarte nicht mehr ganz zeitgemäß bzw. auch zu undurchdacht. Das Logo (Weintraube und Paragraph) finde ich auch nicht mehr so passend (und etwas unseriös). Mir wär lieber ein schönen Schriftzug oder ein Logo mit Initialen oder sonst etwas Kreatives, damit das Ganze etwas professioneller wirkt. Meine Lieblingsfarbe ist violett, es kann aber auch gerne hell und dunkel gemischt werden. Ich könnte mir ebenfalls ein Farbspiel mit Kreisen oder Ecken oder sonst etwas vorstellen. Auf der Vorderseite der Visitenkarte hätte ich gerne 'Lena Moosbrugger - Steuerberatung' stehen. Auf der Rückseite dann 'Steuerberaterin MMag. Lena Moosbrugger' und alle Informationen die auch im Anhang zu finden sind. Ganz unten sollen graphisch abgegrenzt beiden Büro-Adressen stehen. So zumindest mal mein Vorschlag, bin aber auch für andere Ideen offen.

```html
<!DOCTYPE html>
<html lang="de">
<head>
<meta charset="utf-8">
<title>Lena Moosbrugger – Steuerberatung Corporate Design</title>
<link rel="stylesheet" href="https://fonts.googleapis.com/css2?family=Playfair+Display:wght@400&family=Arimo:wght@400&display=swap">
<style>
  :root {
    --lilac: #ae77ab;
    --plum: #7b4d8d;
    --ink: #1c1c1c;
    --paper: #ffffff;
    --serif: "Playfair Display", Georgia, serif;
    --sans: "Arimo", Helvetica, Arial, sans-serif;
  }
  * { box-sizing: border-box; margin: 0; padding: 0; }
  html, body { width: 1200px; height: 1200px; overflow: hidden; background: var(--paper); }
  .canvas { position: relative; width: 1200px; height: 1200px; background: var(--paper); }

  /* brand mark: plain circle with wordmark */
  .mark {
    position: absolute; border-radius: 50%;
    border: 1.3px solid var(--lilac);
    display: flex; align-items: center; justify-content: center; text-align: center;
    font-family: var(--serif); font-weight: 400; color: var(--plum);
    line-height: 1.15; transform: translate(-50%, -50%);
  }
  .mark--light { border-color: #fff; color: #fff; }

  .sheet { position: absolute; background: var(--paper); box-shadow: 0 1px 4px rgba(0,0,0,.35); overflow: hidden; }

  /* letterhead */
  .letterhead { left: 36px; top: 379px; width: 492px; height: 706px; }
  .header-frame { position: absolute; left: 20px; top: 23px; width: 452px; height: 103px; border: 1px solid var(--plum); }
  .frame-name {
    position: absolute; left: 50%; bottom: 0; transform: translate(-50%, 50%);
    padding: 0 7px; font-family: var(--serif); color: var(--lilac);
    white-space: nowrap; letter-spacing: .01em; background: var(--paper);
  }
  .letter-body { position: absolute; left: 20px; top: 187px; width: 416px; font-family: var(--sans); color: var(--ink); }
  .salutation { font-size: 9px; margin-bottom: 32px; }
  .letter-body p { font-size: 9px; line-height: 15px; text-align: justify; margin-bottom: 15px; }
  .signature { position: absolute; left: 20px; top: 446px; width: 106px; height: 63px; background: linear-gradient(135deg, #f2eef2, #e4dde5); }
  .signer { position: absolute; left: 20px; top: 525px; font-family: var(--sans); font-size: 9.5px; color: var(--ink); }
  .letter-footer { position: absolute; left: 0; bottom: 0; width: 100%; height: 99px; background: var(--lilac); font-family: var(--sans); color: #f6edf5; font-size: 8px; }
  .letter-footer .contact { position: absolute; left: 19px; top: 20px; line-height: 14.5px; }
  .letter-footer .offices { position: absolute; right: 24px; top: 26px; text-align: right; line-height: 10px; }
  .letter-footer .offices .office + .office { margin-top: 6px; }

  /* business cards */
  .card { width: 300px; height: 220px; }
  .card--filled { background: var(--lilac); }
  .card-frame { position: absolute; border: 1px solid var(--plum); }
  .card--filled .card-frame { border-color: #fff; }
  .card--filled .frame-name { background: var(--lilac); color: #fff; }
  .card-inset { position: absolute; left: 10px; top: 12px; width: 280px; height: 195px; background: var(--paper); }

  .card-back .back-frame { position: absolute; left: 11px; top: 10px; width: 278px; height: 77px; border: 1px solid var(--plum); }
  .card-back .back-frame .frame-name { color: var(--plum); font-size: 8.5px; letter-spacing: .04em; }
  .card-back .holder { position: absolute; top: 106px; width: 100%; text-align: center; font-family: var(--serif); font-variant: small-caps; color: var(--plum); font-size: 10px; letter-spacing: .05em; }
  .card-back .details { position: absolute; top: 134px; width: 100%; text-align: center; font-family: var(--sans); color: #9a9a9a; font-size: 7px; line-height: 11px; }
  .card-back .details .gap { margin-top: 5px; }
  .card-back .band { position: absolute; left: 0; bottom: 0; width: 100%; height: 37px; background: var(--lilac); font-family: var(--sans); color: #f6edf5; font-size: 6.3px; line-height: 10px; }
  .card-back .band .left { position: absolute; left: 11px; top: 8px; }
  .card-back .band .right { position: absolute; right: 11px; top: 8px; text-align: right; }
</style>
</head>
<body>
<main class="canvas">

  <!-- primary brand mark -->
  <div class="mark" style="left:561px; top:206px; width:184px; height:184px; font-size:17px;">Lena<br>Moosbrugger</div>

  <!-- letterhead -->
  <article class="sheet letterhead">
    <div class="header-frame">
      <div class="mark" style="left:226px; top:48px; width:68px; height:68px; font-size:7px;">Lena<br>Moosbrugger</div>
      <span class="frame-name" style="font-size:13px;">LENA MOOSBRUGGER</span>
    </div>
    <div class="letter-body">
      <div class="salutation">DEAR BERGER,</div>
      <p>Lorem ipsum dolor sit amet, consectetuer adipiscing elit, sed diam nonummy nibh euismod tincidunt ut laoreet dolore magna aliquam erat volutpat. Ut wisi enim ad minim veniam, quis nostrud exerci tation ullamcorper suscipit lobortis nisl ut aliquip ex ea commodo consequat.</p>
      <p>Duis autem vel eum iriure dolor in hendrerit in vulputate velit esse molestie consequat, vel illum dolore eu feugiat nulla facilisis at vero eros et accumsan et iusto odio dignissim qui blandit praesent luptatum zzril delenit augue duis dolore te feugait nulla facilisi.</p>
      <p>Lorem ipsum dolor sit amet, cons ectetuer adipiscing elit, sed diam nonummy nibh euismod tincidunt ut laoreet dolore magna aliquam erat volutpat. Ut wisi enim ad minim veniam, quis nostrud exerci tation ullamcorper suscipit lobortis nisl ut aliquip ex ea commodo consequat.</p>
    </div>
    <div class="signature" role="img" aria-label="Handschriftliche Unterschrift"></div>
    <div class="signer">Lena Moosbrugger</div>
    <footer class="letter-footer">
      <div class="contact">
        Mobil: +43 660 12 34 567<br>
        E-Mail: office@steuerberatung-moosbrugger.at<br>
        Web: www. steuerberatung-moosbrugger.at<br>
        UID: AT...
      </div>
      <div class="offices">
        <div class="office">BÜRO STEIERMARK:<br>Birkenweg 12, 8530 Deutschlandsberg</div>
        <div class="office">BÜRO WIEN:<br>Lindengasse 4, 1070 Wien</div>
      </div>
    </footer>
  </article>

  <!-- card front, filled -->
  <section class="sheet card card--filled" style="left:551px; top:381px;">
    <div class="card-frame" style="left:10px; top:10px; width:281px; height:196px;">
      <span class="frame-name" style="font-size:13px;">LENA MOOSBRUGGER</span>
    </div>
    <div class="mark mark--light" style="left:152px; top:110px; width:114px; height:114px; font-size:11px;">Lena<br>Moosbrugger</div>
  </section>

  <!-- card front, inset -->
  <section class="sheet card card--filled" style="left:871px; top:379px;">
    <div class="card-inset">
      <div class="card-frame" style="left:8px; top:7px; width:264px; height:181px;">
        <span class="frame-name" style="font-size:13px;">LENA MOOSBRUGGER</span>
      </div>
      <div class="mark" style="left:141px; top:99px; width:106px; height:106px; font-size:10.5px;">Lena<br>Moosbrugger</div>
    </div>
  </section>

  <!-- card front, white -->
  <section class="sheet card" style="left:551px; top:624px;">
    <div class="card-frame" style="left:10px; top:12px; width:281px; height:196px;">
      <span class="frame-name" style="font-size:13px;">LENA MOOSBRUGGER</span>
    </div>
    <div class="mark" style="left:153px; top:112px; width:114px; height:114px; font-size:11px;">Lena<br>Moosbrugger</div>
  </section>

  <!-- card back -->
  <section class="sheet card card-back" style="left:871px; top:624px;">
    <div class="back-frame">
      <div class="mark" style="left:140px; top:36px; width:54px; height:54px; font-size:6px;">Lena<br>Moosbrugger</div>
      <span class="frame-name">STEUERBERATERIN</span>
    </div>
    <div class="holder">MMag. Lena Moosbrugger, LL.M.</div>
    <div class="details">
      <div>Mobil: +43 660 12 34 567</div>
      <div class="gap">E-Mail: office@steuerberatung-moosbrugger.at</div>
      <div>Web: www.steuerberatung-moosbrugger.at</div>
    </div>
    <div class="band">
      <div class="left">BÜRO STEIERMARK:<br>Birkenweg, 8530 Deutschlandsberg</div>
      <div class="right">BÜRO WIEN:<br>Lindengasse 4, 1070 Wien</div>
    </div>
  </section>

  <!-- brand mark variants -->
  <div class="mark" style="left:708px; top:984px; width:182px; height:182px; font-size:17px;">Lena<br>Moosbrugger</div>
  <div class="mark" style="left:985px; top:984px; width:182px; height:182px; font-size:17px;">Lena<br>Moosbrugger</div>

</main>
</body>
</html>
```